Keep Climbing - Nobody Writes My Ending

The front book cover. The book will include life lessons I've learned through three breast cancer (Teal Lantern) diagnoses and how to create positivity through adversity. Lessons that most people don't think of until they're hit with a life-altering setback. The chapters include Imposter Syndrome (Teal Lantern Warriors don't have time to debate if they're good enough, they just jump in and get it done because life is too short), Stand Your Ground (stick up for your beliefs and advocate for yourself), The Flip Side of It's All About Me (like an emergency rescuer who must equip themselves first, you need to take care of yourself first). The main message in the book is when others say you CAN'T, I say you CAN! Warrior means being strong no matter what life deals you. I've included a word document with more information.

Please note: Pink is only to be an accent color. I'd like my brand colors to be included. The title of the book is to be the focus with an image to add to the book cover appeal.

Target Market(s)

professionals with a growth mindset and people going through adversity

Industry/Entity Type

HR, Libraries, Hosppitality,

Font styles to use
Sans Serif

Colors
6B429C
8869AF
B7A5CE
E3DAEB
F3F0F8

Requirements
Must have
• Be original. Cover to be appealing to male and female buyers. Incorporate my purple brand color. Be creative and unique.
Nice to have
• Although I have offered a suggestion, I'm open to a creative cover that wows me.
Should not have
• No cartoon image or stock image

```html
<!DOCTYPE html>
<html lang="en">
<head>
<meta charset="utf-8">
<title>Keep Climbing – Nobody Writes My Ending · Cover Concepts</title>
<link href="https://fonts.googleapis.com/css2?family=Outfit:wght@700;800&family=Manrope:wght@600;700&family=Oswald:wght@500&display=swap" rel="stylesheet">
<style>
  :root {
    --page: #f7f7f7;
    --paper: #fbfbfb;
    --brand-purple: #6b429c;
    --title-purple: #7a3f9c;
    --deep-purple: #5a2a82;
    --night-purple: #3e1a5c;
    --magenta: #ef1fa8;
    --rose: #e5398a;
    --rose-deep: #c4246e;
    --blush: #f6d3ea;
    --blush-deep: #f0bfe0;
    --hot-band: #e2178f;
    --lavender: #b7a5ce;
    --ink: #1b1b1b;
    --white: #ffffff;
  }
  * { box-sizing: border-box; margin: 0; padding: 0; }
  html, body { width: 1200px; height: 624px; overflow: hidden; background: var(--page); }
  .canvas { position: relative; width: 1200px; height: 624px; }

  .cover {
    position: absolute; overflow: hidden; background: var(--paper);
    box-shadow: 0 6px 14px rgba(0,0,0,.18);
  }
  .cover--purple { left: 100px; top: 102px; width: 273px; height: 437px; }
  .cover--rose   { left: 455px; top: 98px;  width: 283px; height: 453px; }
  .cover--blush  { left: 834px; top: 109px; width: 267px; height: 426px; background: linear-gradient(180deg, var(--blush) 0%, var(--blush-deep) 100%); }

  .band { position: absolute; left: 0; right: 0; bottom: 0; }
  .cover--purple .band { top: 313px; background: linear-gradient(180deg, var(--deep-purple), var(--night-purple)); }
  .cover--rose .band { top: 276px; background: linear-gradient(180deg, var(--rose) 0%, var(--rose-deep) 100%); }
  .cover--blush .band { top: 396px; background: var(--hot-band); }

  .artwork { position: absolute; }
  .cover--purple .artwork { left: 63px; top: 162px; right: 0; bottom: 0;
    background: linear-gradient(160deg, #f0c7a8 0%, #d99b7a 40%, #222 75%, #111 100%); border-radius: 40% 0 0 0; }
  .cover--rose .artwork { left: 69px; top: 158px; right: 0; bottom: 0;
    background: linear-gradient(165deg, #e7c28a 0%, #f1c6a8 30%, #d9937a 55%, #1a1a1a 80%, #111 100%); border-radius: 45% 30% 0 0; }
  .cover--blush .artwork { left: 97px; top: 164px; width: 72px; height: 173px;
    background: linear-gradient(180deg, #ffffff 0%, #f4dcea 40%, #e25ba5 100%); border-radius: 30px 30px 10px 10px; }

  .title {
    position: absolute; left: 0; right: 0; display: flex; flex-direction: column; align-items: center;
    font-family: "Outfit", sans-serif; font-weight: 800; color: var(--title-purple);
    line-height: .92; letter-spacing: -.5px; text-align: center;
  }
  .cover--purple .title { top: 24px; }
  .cover--rose .title { top: 24px; }
  .cover--blush .title { top: 24px; }

  .title__kicker { display: flex; align-items: center; gap: 8px; font-size: 30px; }
  .title__kicker::before, .title__kicker::after { content: ""; width: 40px; height: 3px; background: var(--title-purple); }
  .title__accent { font-size: 38px; color: var(--magenta); }
  .title__line { font-size: 29px; }
  .title__punch { font-size: 31px; }

  .cover--rose .title__accent { color: var(--rose); font-size: 40px; }
  .cover--rose .title__line { font-size: 30px; }
  .cover--rose .title__punch { font-size: 40px; color: #5e2d7e; }

  .cover--blush .title__kicker { font-size: 32px; }
  .cover--blush .title__kicker::before, .cover--blush .title__kicker::after { width: 46px; }
  .cover--blush .title__accent { font-size: 40px; background: linear-gradient(90deg, #6b2f8e, #a45bc7, #6b2f8e); -webkit-background-clip: text; background-clip: text; color: transparent; }
  .cover--blush .title__line { font-size: 30px; color: #5e2d7e; }
  .cover--blush .title__punch { font-size: 40px; color: #4e2270; }

  .tagline {
    position: absolute; left: 0; right: 0; display: flex; flex-direction: column; align-items: center;
    font-family: "Manrope", sans-serif; font-weight: 700; font-size: 11px; letter-spacing: .8px; color: var(--white);
  }
  .cover--purple .tagline { top: 373px; }
  .cover--rose .tagline { top: 387px; }
  .cover--blush .tagline { top: 350px; color: var(--ink); }
  .tagline__badge { margin-top: 3px; padding: 1px 8px; background: var(--magenta); color: var(--white); }
  .cover--rose .tagline__badge { background: var(--rose-deep); }

  .author {
    position: absolute; left: 0; right: 0; text-align: center;
    font-family: "Oswald", sans-serif; font-weight: 500; font-size: 17px; letter-spacing: 1.6px; color: var(--white);
  }
  .cover--purple .author { top: 402px; }
  .cover--rose .author { top: 415px; }
  .cover--blush .author { top: 399px; font-size: 15px; }
</style>
</head>
<body>
<main class="canvas">

  <article class="cover cover--purple">
    <div class="band"></div>
    <div class="artwork" role="img" aria-label="Photo of a woman in a black tank top flexing her arm, her head covered by a magenta shield, a ribbon wrapped around her arm"></div>
    <h1 class="title">
      <span class="title__kicker">Keep</span>
      <span class="title__accent">CLIMBING</span>
      <span class="title__line">Nobody Writes</span>
      <span class="title__punch">MY ENDING!</span>
    </h1>
    <div class="tagline"><span>Life Lessons from a</span><span class="tagline__badge">3X Teal Warrior</span></div>
    <p class="author">RJ HOLLOWAY, CCMS, MCVP, CSP</p>
  </article>

  <article class="cover cover--rose">
    <div class="band"></div>
    <div class="artwork" role="img" aria-label="Photo of a woman with a red bandana flexing her arm in a black tank top, a ribbon wrapped around her arm"></div>
    <h1 class="title">
      <span class="title__kicker">Keep</span>
      <span class="title__accent">CLIMBING</span>
      <span class="title__line">Nobody Writes</span>
      <span class="title__punch">MY ENDING!</span>
    </h1>
    <div class="tagline"><span>Life Lessons from a</span><span class="tagline__badge">3X Teal Warrior</span></div>
    <p class="author">RJ HOLLOWAY, CCMS, MCVP, CSP</p>
  </article>

  <article class="cover cover--blush">
    <div class="band"></div>
    <div class="artwork" role="img" aria-label="Illustration of a raised fist with an awareness ribbon looped around the wrist"></div>
    <h1 class="title">
      <span class="title__kicker">Keep</span>
      <span class="title__accent">CLIMBING</span>
      <span class="title__line">Nobody Writes</span>
      <span class="title__punch">MY ENDING!</span>
    </h1>
    <div class="tagline"><span>Life Lessons from a</span><span class="tagline__badge">3X Teal Warrior</span></div>
    <p class="author">RJ HOLLOWAY, CCMS, MCVP, CSP</p>
  </article>

</main>
</body>
</html>
```